Verpackungsetikett für Softeisbecher
Zielgruppe
Wir produzieren Speiseeis, füllen dieses in entsprechende Verpackungseinheiten ab und vermarkten es. Zielgruppe sind alle die, die Eis mögen.
Aufgabenstellung
Das bestehende Etikettendesign (rund 8cm Durchmesser) soll neu überarbeitet werden. Dazu soll es mit unserem neuen Logo (Anhang) versehen werden. Wir freuen uns über fotolose Vorschläge bzw. Design´s mit Foto. Alle Angaben über z.B. Inhaltstoffe, Herstellungdatum, Aufbewahrungtemperatur, Barcode u.s.w.kommen auf ein separates Etikett am Boden des Bechers.Das Erscheinungsbild des Etiketts sollte eine gewisse Neutralität haben, so dass es für die verschiedensten Geschmacksrichtungen verwendet werden kann, sprich ein Etikett für alle Eissorten. Nur der Name der Geschmacksrichtung unterscheidet die Etiketten. Wir verweisen auf einige Link`s ,auf denen man Etikettenbeispiele (z. B. Frischkäse) sieht, die unseren Vorstellungen der Gestaltung entsprechen. Vielen Dank im Voraus

```html
<!DOCTYPE html>
<html lang="de">
<head>
<meta charset="utf-8">
<title>Softeis Etikett – Erdbeer Joghurt</title>
<link rel="stylesheet" href="https://fonts.googleapis.com/css2?family=Lora:ital,wght@0,700;1,700&display=swap">
<style>
  :root {
    --page-bg: #ffffff;
    --ring-blue: #2a8fd0;
    --ring-blue-light: #8fd0f2;
    --band-red: #d8231c;
    --band-red-dark: #b8171a;
    --banner-gold: #d99a2b;
    --banner-gold-light: #f2c15a;
    --title-blue: #1b4f9c;
    --brand-green: #8ab83a;
    --label-white: #ffffff;
    --glow-green: #dcebc4;
    --milk: #eef1f3;
    --berry: #d9262e;
    --berry-dark: #a8141d;
  }
  html, body {
    margin: 0;
    width: 1200px;
    height: 1200px;
    overflow: hidden;
    background: var(--page-bg);
  }
  .label {
    display: block;
    width: 1200px;
    height: 1200px;
  }
  .brand-name {
    font-family: "Lora", Georgia, serif;
    font-weight: 700;
    font-size: 58px;
    fill: var(--brand-green);
  }
  .product-title {
    font-family: "Lora", Georgia, serif;
    font-weight: 700;
    font-size: 170px;
    fill: var(--title-blue);
  }
  .banner-slogan {
    font-family: "Lora", Georgia, serif;
    font-style: italic;
    font-weight: 700;
    font-size: 48px;
    fill: var(--label-white);
  }
  .banner-flavour {
    font-family: "Lora", Georgia, serif;
    font-style: italic;
    font-weight: 700;
    font-size: 40px;
    fill: var(--label-white);
  }
</style>
</head>
<body>
<svg class="label" viewBox="0 0 1200 1200" xmlns="http://www.w3.org/2000/svg">
  <defs>
    <clipPath id="label-face">
      <circle cx="600" cy="600" r="480"/>
    </clipPath>
    <radialGradient id="green-glow" cx="0.72" cy="0.32" r="0.55">
      <stop offset="0" stop-color="var(--glow-green)"/>
      <stop offset="1" stop-color="var(--label-white)"/>
    </radialGradient>
    <linearGradient id="milk-splash" x1="0" y1="0" x2="1" y2="1">
      <stop offset="0" stop-color="var(--label-white)"/>
      <stop offset="1" stop-color="var(--milk)"/>
    </linearGradient>
    <radialGradient id="berries" cx="0.5" cy="0.55" r="0.5">
      <stop offset="0" stop-color="var(--berry)"/>
      <stop offset="0.75" stop-color="var(--berry-dark)"/>
      <stop offset="1" stop-color="var(--milk)" stop-opacity="0"/>
    </radialGradient>
    <linearGradient id="gold-banner" x1="0" y1="0" x2="1" y2="0">
      <stop offset="0" stop-color="var(--banner-gold)"/>
      <stop offset="1" stop-color="var(--banner-gold-light)"/>
    </linearGradient>
    <linearGradient id="red-banner" x1="0" y1="0" x2="1" y2="0">
      <stop offset="0" stop-color="var(--band-red-dark)"/>
      <stop offset="1" stop-color="var(--band-red)"/>
    </linearGradient>
  </defs>

  <g class="label-face" clip-path="url(#label-face)">
    <rect x="120" y="120" width="960" height="960" fill="url(#green-glow)"/>
    <path class="milk-splash" role="img" aria-label="Milchspritzer"
          d="M120 580 C260 540 380 620 520 660 C700 710 860 670 1080 580 L1080 1080 L120 1080 Z"
          fill="url(#milk-splash)"/>
    <ellipse class="strawberries" role="img" aria-label="Frische Erdbeeren im Joghurt"
             cx="770" cy="850" rx="200" ry="140" fill="url(#berries)"/>
    <ellipse class="strawberry-top" role="img" aria-label="Erdbeere"
             cx="700" cy="720" rx="70" ry="50" fill="url(#berries)"/>
  </g>

  <circle class="rim-blue" cx="600" cy="600" r="462" fill="none" stroke="var(--ring-blue)" stroke-width="36"/>
  <circle class="rim-stripe" cx="600" cy="600" r="436" fill="none" stroke="var(--ring-blue-light)" stroke-width="8"/>
  <path class="rim-red" d="M1049 720 A465 465 0 0 1 151 720" fill="none" stroke="var(--band-red)" stroke-width="44"/>

  <text class="brand-name" x="600" y="420" text-anchor="middle">Wendelmoor</text>

  <text class="product-title" x="600" y="630" text-anchor="middle">Softeis</text>

  <g class="banners" transform="rotate(-5 400 800)">
    <rect class="banner-gold" x="140" y="750" width="520" height="64" fill="url(#gold-banner)"/>
    <text class="banner-slogan" x="180" y="798">mmh… so lecker!</text>
    <rect class="banner-red" x="190" y="822" width="450" height="68" fill="url(#red-banner)"/>
    <text class="banner-flavour" x="222" y="869">Erdbeer Joghurt</text>
  </g>
</svg>
</body>
</html>
```